Menu design for a modern Pizza restaurant

We need a menu design which is visually attractive but also user friendly.
We want it to be A3 but fold in just like the Tonk'd menu attached.
We also want colourful and fun like our branding is.
I have attached another menu example from Ul Pizza which is laid out very well but needs colour.
Also attached is Merno menu which we like the design of, just needs colour.
Attached is our imagery and logo.
And lastly is our menu attached.
We really need it in 24 hours if possible.

Target Market(s)

All Pizza eaters in our area

Industry/Entity Type

Hospitality

Requirements
Must have
• Bold, colourful and fun

```html
<!DOCTYPE html>
<html lang="en">
<head>
<meta charset="utf-8">
<title>Forno Lab – Folded Menu</title>
<link href="https://fonts.googleapis.com/css2?family=Archivo:wght@400;500;700&family=Roboto+Condensed:wght@700&display=swap" rel="stylesheet">
<style>
  :root {
    --tomato: #ec5235;
    --tomato-deep: #d9432b;
    --tomato-light: #f26a4c;
    --sea: #2d7ea6;
    --sea-light: #4aa6c8;
    --sea-deep: #226a90;
    --mint: #8fd6cf;
    --backdrop: #5fb0c6;
    --backdrop-deep: #3d93b0;
    --paper: #ffffff;
  }
  * { box-sizing: border-box; margin: 0; padding: 0; }
  html, body { width: 848px; height: 1200px; overflow: hidden; }
  body {
    background: linear-gradient(160deg, var(--backdrop-deep), var(--backdrop));
    font-family: "Archivo", Arial, sans-serif;
    color: var(--paper);
    position: relative;
  }
  .sheet {
    position: absolute; left: 224px; width: 400px; height: 566px; overflow: hidden;
  }
  .sheet--cover { top: 24px; }
  .sheet--inside { top: 610px; }

  /* Cover */
  .cover-pattern {
    position: absolute; inset: 0;
    background: linear-gradient(135deg, var(--tomato) 0%, var(--tomato-light) 35%, #e8604a 60%, var(--tomato) 100%);
  }
  .fold { position: absolute; background: rgba(0,0,0,.08); }
  .fold--v { left: 199px; top: 0; width: 2px; height: 100%; }
  .fold--h { top: 282px; left: 0; height: 2px; width: 100%; }
  .cover-disc {
    position: absolute; left: 118px; top: 384px; width: 108px; height: 108px;
    border-radius: 50%; background: var(--mint);
  }
  .cover-name {
    position: absolute; left: 248px; top: 370px;
    font-family: "Roboto Condensed", "Arial Narrow", sans-serif;
    font-weight: 700; font-size: 24px; letter-spacing: 1px; text-transform: uppercase;
  }

  /* Inside */
  .inside-border {
    position: absolute; inset: 0;
    background: linear-gradient(135deg, var(--tomato), var(--tomato-light), var(--tomato));
  }
  .menu-sheet {
    position: absolute; left: 10px; top: 10px; width: 380px; height: 546px;
    border: 2px solid var(--paper); overflow: hidden;
  }
  .masthead {
    position: absolute; left: 0; top: 0; width: 100%; height: 40px;
    background: linear-gradient(90deg, var(--sea-deep), var(--sea));
    border-bottom: 2px solid var(--paper);
    display: flex; align-items: center; justify-content: center;
  }
  .brand-name {
    font-family: "Roboto Condensed", "Arial Narrow", sans-serif;
    font-weight: 700; font-size: 20px; letter-spacing: 1px; text-transform: uppercase;
  }
  .col-pizza {
    position: absolute; left: 0; top: 40px; width: 192px; height: 330px;
    background: linear-gradient(180deg, var(--sea) 0%, var(--sea-light) 55%, var(--sea) 100%);
    border-right: 2px solid var(--paper);
    padding: 7px 10px;
  }
  .col-extras {
    position: absolute; left: 192px; top: 40px; width: 184px; height: 330px;
    background: linear-gradient(180deg, var(--tomato-deep), var(--tomato));
    padding: 7px 10px;
  }
  .section-title {
    font-size: 19px; font-weight: 500; line-height: 1;
    display: flex; align-items: baseline; gap: 6px;
    border-bottom: 1.5px solid var(--paper); padding-bottom: 3px; margin-bottom: 5px;
  }
  .section-price { font-size: 6px; font-weight: 400; margin-left: auto; }
  .dish { margin-bottom: 4px; }
  .dish-name { font-size: 8px; font-weight: 700; line-height: 1.15; display: flex; }
  .dish-cost { margin-left: auto; font-weight: 500; font-size: 7px; }
  .dish-desc { font-size: 5.5px; line-height: 1.25; opacity: .9; }
  .extras-block { margin-bottom: 12px; }
  .build-panel {
    position: absolute; left: 0; top: 370px; width: 100%; height: 172px;
    background: linear-gradient(135deg, var(--tomato), var(--tomato-deep));
    border-top: 2px solid var(--paper);
    padding: 10px 12px;
    display: flex; gap: 12px;
  }
  .build-intro { width: 140px; }
  .build-kicker { font-size: 9px; }
  .build-title { font-weight: 500; font-size: 30px; line-height: .9; margin: 3px 0 8px; }
  .build-title .big { font-size: 40px; }
  .build-pricing { font-size: 6.5px; line-height: 1.4; }
  .build-options {
    flex: 1; border-left: 1.5px solid var(--paper); padding-left: 10px;
    display: grid; grid-template-columns: 50px 1fr; row-gap: 6px; column-gap: 6px;
    align-content: start;
  }
  .option-label { font-size: 7px; font-weight: 700; }
  .option-list { font-size: 6px; line-height: 1.3; }
</style>
</head>
<body>
  <section class="sheet sheet--cover">
    <div class="cover-pattern" role="img" aria-label="Geometric triangle pattern in tomato red and sea blue covering the folded menu front"></div>
    <span class="fold fold--v"></span>
    <span class="fold fold--h"></span>
    <span class="cover-disc"></span>
    <span class="cover-name">Forno Lab</span>
  </section>

  <section class="sheet sheet--inside">
    <div class="inside-border" role="img" aria-label="Triangle pattern border in tomato red and sea blue"></div>
    <main class="menu-sheet">
      <header class="masthead"><span class="brand-name">Forno Lab</span></header>

      <section class="col-pizza">
        <h2 class="section-title">Pizza <span class="section-price">11 inch $13 / 13 inch $16</span></h2>
        <div class="dish"><div class="dish-name">Slow pork buffalo</div><div class="dish-desc">Pulled pork, buffalo sauce</div></div>
        <div class="dish"><div class="dish-name">Duck and nectarine</div><div class="dish-desc">Roast duck, hoisin, coriander</div></div>
        <div class="dish"><div class="dish-name">Supreme</div><div class="dish-desc">Ham, salami, capsicum, olives</div></div>
        <div class="dish"><div class="dish-name">Pepperoni</div><div class="dish-desc">Tomato, mozzarella, pepperoni</div></div>
        <div class="dish"><div class="dish-name">Tropical</div><div class="dish-desc">Smoked ham, pineapple</div></div>
        <div class="dish"><div class="dish-name">Margherita</div><div class="dish-desc">Tomato, fior di latte, basil</div></div>
        <div class="dish"><div class="dish-name">Mushroom deluxe</div><div class="dish-desc">Field mushrooms, garlic, thyme</div></div>
        <div class="dish"><div class="dish-name">Prawn and chilli</div><div class="dish-desc">Garlic prawns, rocket, lemon</div></div>
        <div class="dish"><div class="dish-name">Formaggi amore</div><div class="dish-desc">Four cheeses, honey</div></div>
        <div class="dish"><div class="dish-name">Garlic pizza</div><div class="dish-desc">Garlic butter, parsley</div></div>
        <div class="dish"><div class="dish-name">Lamb and pumpkin</div><div class="dish-desc">Spiced lamb, feta, mint</div></div>
        <div class="dish"><div class="dish-name">Sing your heart out</div><div class="dish-desc">Chicken, bacon, avocado</div></div>
        <div class="dish"><div class="dish-name">Vegetarian</div><div class="dish-desc">Capsicum, olives, spinach</div></div>
      </section>

      <section class="col-extras">
        <div class="extras-block">
          <h2 class="section-title">Salads <span class="section-price">$14</span></h2>
          <div class="dish"><div class="dish-name">Roast pumpkin and lentil salad</div><div class="dish-desc">Pumpkin, feta, rocket</div></div>
          <div class="dish"><div class="dish-name">Rocket and parmesan</div><div class="dish-desc">Pear, walnuts, parmesan</div></div>
        </div>
        <div class="extras-block">
          <h2 class="section-title">Pasta/Gnocchi <span class="section-price">$16</span></h2>
          <div class="dish"><div class="dish-name">Potato gnocchi</div><div class="dish-desc">Napoli, basil, parmesan</div></div>
          <div class="dish"><div class="dish-name">Penne carbonara</div><div class="dish-desc">Pancetta, egg, pecorino</div></div>
        </div>
        <div class="extras-block">
          <h2 class="section-title">Sides</h2>
          <div class="dish"><div class="dish-name">Chips &amp; aioli <span class="dish-cost">$8</span></div></div>
          <div class="dish"><div class="dish-name">Garlic bread <span class="dish-cost">$7</span></div></div>
          <div class="dish"><div class="dish-name">Chicken wings <span class="dish-cost">$12</span></div></div>
          <div class="dish"><div class="dish-name">Arancini balls <span class="dish-cost">$10</span></div></div>
        </div>
      </section>

      <section class="build-panel">
        <div class="build-intro">
          <p class="build-kicker">Your own Forno:</p>
          <h2 class="build-title">Build<br>your own<br><span class="big">PIZZA</span></h2>
          <p class="build-pricing">Pizza pricing:<br>Kids $8 / Small $12<br>Regular $16 / Share $20</p>
        </div>
        <div class="build-options">
          <span class="option-label">Base</span><span class="option-list">Classic, thin, gluten free</span>
          <span class="option-label">Sauce</span><span class="option-list">Tomato, BBQ, pesto</span>
          <span class="option-label">Meat</span><span class="option-list">Ham, salami, chicken, bacon</span>
          <span class="option-label">Veggies</span><span class="option-list">Mushroom, onion, olives</span>
          <span class="option-label">Cheese</span><span class="option-list">Mozzarella, feta, parmesan</span>
          <span class="option-label">Dairy free</span><span class="option-list">Vegan cheese</span>
          <span class="option-label">Fruit &amp; herbs</span><span class="option-list">Pineapple, basil, chilli</span>
          <span class="option-label">Seafood</span><span class="option-list">Prawns, anchovies</span>
        </div>
      </section>
    </main>
  </section>
</body>
</html>
```